IT services company requires Letterhead design

We need a professional letterhead designed to be used for general correspondence with customers, quotes, invoices etc. We are a new IT services company specialising in computer servicing and repairs and mobile and tablet repairs. Attached are templates that my printing company have supplied, my logos, an interpretation of our website for you to get a feel of the company. Details to be included on the letterhead are

Company Number – 4830517
VAT Number - 581736294
Registered Address – 14-16 Brambury Lane, London, E9 3PL

Phone – 01843 572236
Email – sales@quorvant.com
Web – www.quorvant.com

I would prefer for the top of the letterhead to just have the company logo on a white background and the rest of the details on the bottom of the letterhead but I am open to design ideas.

Thanks

```html
<!DOCTYPE html>
<html lang="en">
<head>
<meta charset="utf-8">
<title>Quorvant Letterhead</title>
<link rel="stylesheet" href="https://fonts.googleapis.com/css2?family=Open+Sans:wght@400;700&display=swap">
<style>
  :root {
    --backdrop: #d9d9d9;
    --paper: #ffffff;
    --brand-cyan: #2bc0e0;
    --brand-charcoal: #36383c;
    --ink-grey: #555a60;
    --rule-grey: #b9bcc0;
  }
  html, body {
    margin: 0;
    padding: 0;
    width: 1200px;
    height: 936px;
    overflow: hidden;
    background: var(--backdrop);
    font-family: "Open Sans", Arial, sans-serif;
  }
  .letterhead {
    position: absolute;
    left: 296px;
    top: 38px;
    width: 608px;
    height: 860px;
    background: var(--paper);
    box-shadow: 0 6px 18px rgba(0,0,0,0.18);
    overflow: hidden;
  }
  .brand {
    position: absolute;
    left: 40px;
    top: 40px;
    display: flex;
    align-items: center;
    gap: 8px;
  }
  .brand-mark {
    width: 14px;
    height: 14px;
    background: var(--brand-charcoal);
  }
  .brand-name {
    font-size: 26px;
    font-weight: 700;
    color: var(--brand-cyan);
    letter-spacing: 0.2px;
  }
  .registration {
    position: absolute;
    right: 40px;
    top: 40px;
    padding-left: 10px;
    border-left: 1px solid var(--rule-grey);
    font-size: 9.5px;
    line-height: 15px;
    color: var(--ink-grey);
  }
  .footer-wave {
    position: absolute;
    left: 0;
    top: 0;
    width: 608px;
    height: 860px;
  }
  .contact {
    position: absolute;
    right: 18px;
    bottom: 10px;
    display: flex;
    flex-direction: column;
    align-items: flex-end;
    gap: 4px;
    font-size: 10px;
    line-height: 14px;
    color: var(--paper);
    white-space: nowrap;
  }
  .contact-line {
    display: flex;
    align-items: center;
    gap: 9px;
  }
  .contact-item {
    display: inline-flex;
    align-items: center;
    gap: 4px;
  }
  .contact-icon {
    width: 10px;
    height: 10px;
    flex: none;
  }
</style>
</head>
<body>
  <main class="letterhead">
    <svg class="footer-wave" viewBox="0 0 608 860" aria-hidden="true">
      <path d="M0 814 C150 804 320 766 440 742 C520 726 570 762 608 780 L608 860 L0 860 Z" fill="var(--brand-charcoal)"/>
      <path d="M0 852 C170 840 330 796 450 772 C530 756 575 782 608 790 L608 860 L0 860 Z" fill="var(--brand-cyan)" stroke="var(--paper)" stroke-width="3"/>
    </svg>

    <header class="brand">
      <span class="brand-mark"></span>
      <span class="brand-name">Quorvant</span>
    </header>

    <aside class="registration">
      <div>Company Number – 4830517</div>
      <div>VAT Number - 581736294</div>
    </aside>

    <footer class="contact">
      <div class="contact-line">
        <span class="contact-item">
          <svg class="contact-icon" viewBox="0 0 10 10"><circle cx="5" cy="5" r="5" fill="#fff"/><circle cx="5" cy="4.2" r="1.6" fill="var(--brand-cyan)"/></svg>
          14-16 Brambury Lane, London, E9 3PL
        </span>
      </div>
      <div class="contact-line">
        <span class="contact-item">
          <svg class="contact-icon" viewBox="0 0 10 10"><circle cx="5" cy="5" r="5" fill="#fff"/><rect x="3.6" y="2.5" width="2.8" height="5" rx="1" fill="var(--brand-cyan)"/></svg>
          01843 572236
        </span>
        <span class="contact-item">
          <svg class="contact-icon" viewBox="0 0 10 10"><circle cx="5" cy="5" r="5" fill="#fff"/><rect x="2.2" y="3.2" width="5.6" height="3.8" fill="var(--brand-cyan)"/></svg>
          sales@quorvant.com
        </span>
        <span class="contact-item">
          <svg class="contact-icon" viewBox="0 0 10 10"><circle cx="5" cy="5" r="5" fill="#fff"/><circle cx="5" cy="5" r="2.8" fill="none" stroke="var(--brand-cyan)" stroke-width="1"/></svg>
          www.quorvant.com
        </span>
      </div>
    </footer>
  </main>
</body>
</html>
```